BOLD & MINIMALIST DESIGN NEEDED

We want a very bold but minimalistic business card design that is impactful and utilizes both sides of the business card. Our current logo is included for your use.

We want bold fonts and good use of negative space. We don't want the logo to overpower the design.

Target Market(s)

Professionals who are building new commercial buildings.

Industry/Entity Type

Construction

Contact Information for Business Card

Name, Title, email, office phone, cell phone, website

Font styles to use
Serif
Sans Serif

Requirements
Must have
• Bold design!

```html
<!DOCTYPE html>
<html lang="en">
<head>
<meta charset="utf-8">
<title>Ridgeline Build Co — Business Card</title>
<link rel="stylesheet" href="https://fonts.googleapis.com/css2?family=Quicksand:wght@500;600;700&display=swap">
<style>
  :root {
    --bg: #e4e5e5;
    --card: #f7f7f6;
    --green: #8dc63f;
    --green-light: #cfe3a6;
    --ink: #2b2b2b;
    --ink-soft: #555555;
    --charcoal: #3a3a3a;
    --shadow: rgba(0, 0, 0, 0.18);
  }
  * { margin: 0; padding: 0; box-sizing: border-box; }
  html, body { width: 1200px; height: 1000px; overflow: hidden; }
  body {
    background: var(--bg);
    font-family: "Quicksand", sans-serif;
    color: var(--ink);
    position: relative;
  }
  .card {
    position: absolute;
    width: 560px;
    height: 360px;
    background: var(--card);
    box-shadow: 0 10px 30px var(--shadow);
    overflow: hidden;
  }

  /* Back side: contact details */
  .card-back { left: 560px; top: 140px; }
  .person-name {
    position: absolute; left: 60px; top: 72px;
    font-size: 24px; font-weight: 700; color: var(--green);
    letter-spacing: 0.5px;
  }
  .person-title {
    position: absolute; left: 60px; top: 104px;
    font-size: 14px; font-weight: 500; color: var(--ink-soft);
  }
  .divider {
    position: absolute; left: 60px; top: 156px;
    width: 60px; height: 2px; background: var(--ink);
  }
  .contact-list { position: absolute; left: 60px; top: 200px; list-style: none; }
  .contact-item {
    display: flex; align-items: center; gap: 10px;
    height: 33px;
    font-size: 18px; font-weight: 500; color: var(--ink);
  }
  .contact-icon {
    width: 22px; height: 22px; border-radius: 50%;
    background: var(--green);
    display: flex; align-items: center; justify-content: center;
  }
  .corner-shapes { position: absolute; left: 0; top: 0; }

  /* Front side: company name */
  .card-front { left: 130px; top: 540px; }
  .brand {
    position: absolute; left: 0; right: 0; top: 150px;
    display: flex; align-items: center; justify-content: center; gap: 14px;
  }
  .brand-mark { width: 26px; height: 26px; background: var(--green); }
  .brand-name {
    font-size: 38px; font-weight: 700; color: var(--ink);
    letter-spacing: 1px;
  }
  .website {
    position: absolute; left: 0; right: 0; top: 314px;
    text-align: center;
    font-size: 15px; font-weight: 500; color: var(--ink-soft);
    letter-spacing: 0.5px;
  }
</style>
</head>
<body>

  <section class="card card-back" aria-label="Card back with contact details">
    <h1 class="person-name">YOUR NAME</h1>
    <p class="person-title">Founder, CEO</p>
    <div class="divider"></div>
    <ul class="contact-list">
      <li class="contact-item">
        <span class="contact-icon">
          <svg width="12" height="12" viewBox="0 0 12 12"><rect x="3" y="1" width="6" height="10" rx="1" fill="none" stroke="#fff" stroke-width="1.3"/></svg>
        </span>
        000.1234.56789
      </li>
      <li class="contact-item">
        <span class="contact-icon">
          <svg width="12" height="12" viewBox="0 0 12 12"><path d="M3 1.5 L5 3.8 L4 5 C4.6 6.4 5.6 7.4 7 8 L8.2 7 L10.5 9 L9.2 10.5 C5.5 10 2 6.5 1.5 2.8 Z" fill="#fff"/></svg>
        </span>
        [00] 0123 5678
      </li>
      <li class="contact-item">
        <span class="contact-icon">
          <svg width="12" height="12" viewBox="0 0 12 12"><rect x="1.5" y="3" width="9" height="6.5" fill="#fff"/><path d="M1.5 3 L6 6.6 L10.5 3" fill="none" stroke="#8dc63f" stroke-width="1"/></svg>
        </span>
        email@yourwebhere.com
      </li>
    </ul>
    <svg class="corner-shapes" width="560" height="360" viewBox="0 0 560 360" aria-hidden="true">
      <polygon points="396,226 445,226 396,297" fill="var(--green-light)"/>
      <polygon points="426,360 537,199 537,360" fill="var(--green)"/>
      <polygon points="537,199 560,242 560,360 537,360" fill="var(--charcoal)"/>
    </svg>
  </section>

  <section class="card card-front" aria-label="Card front with company name">
    <div class="brand">
      <span class="brand-mark"></span>
      <span class="brand-name">RIDGELINE BUILD CO</span>
    </div>
    <p class="website">www.yourwebhere.com</p>
  </section>

</body>
</html>
```